Professional website for software / consulting firm targeting the legal market.
Veranth Systems
Professional website for software / consulting firm targeting the legal market. - Software
Creative Brief
Software
www.veranth.example
The company provides consulting to law firms engaged in mass tort litigation with expertise in data mining and analysis, e-discovery and case management. The company is also engaged in software development with focus on e-discovery collection and analysis.
Like professional looking, easy to navigate websites that aren't cluttered or cumbersome yet informative and efficient.
below header
As we work primarily in the legal space we need to portray our professional, focused image equally coupled with our modern, technology focus bent on problem solving.
kmorlen kmorlen
In addition, I want to clarify our consulting offerings and software. We are focusing on providing software solutions to empower our clients to solve their business challenges. Our brand of consulting doesn't stop at identifying the problem but continues to finding a solution and then implementing the solution. We want to truly focus on our ability to understand the issues and development software solutions for our industry. I hope this helps in your design efforts.
Thank you to all the designers working on this project. Here are my evolving thoughts: 1. Go lighter on written content on the homepage. Information which pertains to About us, services, products and contact us will be placed on those interior pages. With the exception of an info@veranth.example and phone number which should always be available regardless of page. 2. Search features are not needed 3. Client list will not be made available nor highlighted 4. I am leaning towards those designs which are clean and highly professional looking with a tech edge. 5. I like the large initial photo banner which scrolls through several images with tag lines. These remind me of mini-advertisements which need to convey a pointed message in 1 line of words with a good photo.
The tabs for the interior pages on the navigation should be: Home | About Us | Products | Services Please try to keep the landing page design for the homepage to a single page. We would like to keep a clean design with minimal scrolling on information pages. A common theme in the designs is the use of the rotating banners which I like very much and think these are a good way to provide varying pieces of information without having the end user having to scroll down a page. Thank you for the work thus far, I will attempt to provide feedback as quickly as possible on submitted designs.

```html
<!DOCTYPE html>
<html lang="en">
<head>
<meta charset="utf-8">
<title>Veranth Systems</title>
<link rel="stylesheet" href="https://fonts.googleapis.com/css2?family=Open+Sans:wght@300;400;600;700&display=swap">
<style>
  :root {
    --navy: #0d3b66;
    --blue: #135f9a;
    --blue-bright: #1a7cc4;
    --blue-deep: #0a3c64;
    --cyan: #4fd0f0;
    --orange: #f08a24;
    --ink: #2a2a2a;
    --grey-text: #6d7075;
    --grey-light: #eceef0;
    --grey-mid: #d9dcdf;
    --white: #ffffff;
  }
  * { box-sizing: border-box; margin: 0; padding: 0; }
  html, body { width: 1200px; height: 943px; overflow: hidden; }
  body {
    font-family: "Open Sans", Arial, sans-serif;
    background: linear-gradient(#f7f7f8, #e4e6e8);
    position: relative;
    color: var(--ink);
  }
  .site-header {
    position: absolute; left: 0; top: 0; width: 1200px; height: 94px;
    background: var(--white);
    border-bottom: 2px solid var(--blue);
  }
  .brand {
    position: absolute; left: 150px; top: 22px;
    display: flex; align-items: center; gap: 14px;
  }
  .brand-dot {
    width: 44px; height: 44px; border-radius: 50%;
    background: var(--blue);
  }
  .brand-name {
    font-size: 34px; font-weight: 700; color: var(--navy);
    letter-spacing: 0.5px;
  }
  .call-us { position: absolute; left: 890px; top: 22px; }
  .call-us-label { font-size: 15px; color: var(--grey-text); }
  .call-us-number { font-size: 38px; font-weight: 700; color: var(--navy); line-height: 1.05; }

  .main-nav {
    position: absolute; left: 140px; top: 96px; width: 918px; height: 34px;
    background: linear-gradient(#1b6aa6, #0c4477);
    display: flex;
  }
  .main-nav a {
    color: var(--white); text-decoration: none; font-size: 14px;
    line-height: 34px; padding: 0 24px;
    border-right: 1px solid rgba(255,255,255,0.25);
  }
  .main-nav a.active { background: linear-gradient(#f2f3f4, #d6d9dc); color: var(--ink); }

  .hero-intro { position: absolute; left: 140px; top: 212px; width: 440px; }
  .hero-welcome { font-size: 30px; font-weight: 300; color: #3e6f97; }
  .hero-title { font-size: 44px; font-weight: 700; color: var(--blue-bright); line-height: 1.1; }
  .hero-text { margin-top: 14px; font-size: 15px; line-height: 1.45; color: var(--grey-text); }
  .btn {
    display: inline-block; color: var(--white); text-decoration: none;
    background: linear-gradient(#2377b8, #0c4477); border-radius: 3px;
  }
  .btn-read { margin-top: 16px; font-size: 16px; padding: 6px 18px; }

  .monitor { position: absolute; left: 624px; top: 158px; width: 413px; height: 352px; }

  .services-band {
    position: absolute; left: 0; top: 530px; width: 1200px; height: 326px;
    background: linear-gradient(#f4f5f6, #e2e5e7);
  }
  .services-panel { position: absolute; left: 0; top: 530px; }
  .services-title {
    position: absolute; left: 145px; top: 552px;
    font-size: 40px; font-weight: 700; color: var(--white);
  }
  .services-rule { position: absolute; left: 145px; top: 618px; width: 310px; height: 1px; background: rgba(255,255,255,0.35); }
  .services-list { position: absolute; left: 145px; top: 636px; list-style: none; width: 280px; }
  .services-list li {
    display: flex; gap: 10px; font-size: 20px; line-height: 1.15;
    color: var(--white); margin-bottom: 14px;
  }
  .services-list li.current { color: var(--cyan); }
  .services-list svg { flex: none; margin-top: 3px; }

  .feature-title {
    position: absolute; left: 522px; top: 552px;
    font-size: 34px; font-weight: 400; color: #3a5f80;
  }
  .feature-rule { position: absolute; left: 515px; top: 618px; width: 560px; height: 1px; background: var(--grey-mid); }
  .feature-photo {
    position: absolute; left: 505px; top: 637px; width: 170px; height: 133px;
    background: var(--white); padding: 8px; box-shadow: 0 2px 6px rgba(0,0,0,0.25);
  }
  .feature-photo div { width: 100%; height: 100%; background: linear-gradient(135deg, #4a4a48, #2a2b2a); }
  .feature-text {
    position: absolute; left: 700px; top: 637px; width: 260px;
    font-size: 11px; line-height: 1.45; color: #555;
  }
  .feature-text strong { color: var(--ink); }
  .btn-more { position: absolute; left: 700px; top: 750px; width: 103px; text-align: center; font-size: 13px; font-weight: 700; padding: 3px 0; }

  .site-footer {
    position: absolute; left: 0; top: 866px; width: 1200px; height: 77px;
    background: linear-gradient(#e6e8ea, #d3d6d9);
    border-top: 1px solid #c5c9cc;
  }
  .copyright { position: absolute; left: 153px; top: 30px; font-size: 13px; color: var(--grey-text); }
  .footer-brand { position: absolute; left: 840px; top: 20px; display: flex; align-items: center; gap: 10px; }
  .footer-brand .brand-dot { width: 32px; height: 32px; }
  .footer-brand .brand-name { font-size: 24px; }
</style>
</head>
<body>
  <header class="site-header">
    <div class="brand"><span class="brand-dot"></span><span class="brand-name">VERANTH SYSTEMS</span></div>
    <div class="call-us">
      <div class="call-us-label">Call Us Today :</div>
      <div class="call-us-number">555.014.2280</div>
    </div>
  </header>

  <nav class="main-nav">
    <a class="active" href="#">Home</a>
    <a href="#">About Us</a>
    <a href="#">Mining and analysis</a>
    <a href="#">E-discovery and Case management</a>
    <a href="#">FAQ</a>
    <a href="#">Contact Us</a>
  </nav>

  <section class="hero-intro">
    <div class="hero-welcome">Welcome to</div>
    <h1 class="hero-title">Veranth Systems</h1>
    <p class="hero-text">Lorem ipsum dolor sit amet, consectetur adipiscing elit. Aliquam bibendum lacinia nisi, sit amet imperdiet odio. Class aptent taciti sociosqu ad litora.</p>
    <a class="btn btn-read" href="#">Read More</a>
  </section>

  <svg class="monitor" viewBox="0 0 413 352" xmlns="http://www.w3.org/2000/svg">
    <defs>
      <linearGradient id="stand" x1="0" y1="0" x2="0" y2="1">
        <stop offset="0" stop-color="#d8dadd"/><stop offset="1" stop-color="#a9adb1"/>
      </linearGradient>
      <linearGradient id="photo" x1="0" y1="0" x2="1" y2="1">
        <stop offset="0" stop-color="#c9ccd0"/><stop offset="0.6" stop-color="#6b6f75"/><stop offset="1" stop-color="#2c2f34"/>
      </linearGradient>
    </defs>
    <rect x="0" y="0" width="413" height="268" rx="10" fill="#151719"/>
    <rect x="13" y="15" width="387" height="240" fill="url(#photo)" role="img" aria-label="Banner photo: business team meeting around a laptop"/>
    <rect x="13" y="120" width="14" height="24" fill="#1a7cc4"/>
    <path d="M23 125 L17 132 L23 139" stroke="#fff" stroke-width="2" fill="none"/>
    <rect x="386" y="120" width="14" height="24" fill="#1a7cc4"/>
    <path d="M390 125 L396 132 L390 139" stroke="#fff" stroke-width="2" fill="none"/>
    <rect x="0" y="262" width="413" height="18" rx="4" fill="#d7d9dc"/>
    <path d="M175 280 H238 L246 330 H167 Z" fill="url(#stand)"/>
    <ellipse cx="206" cy="336" rx="75" ry="9" fill="#c3c6ca"/>
  </svg>

  <div class="services-band"></div>
  <svg class="services-panel" width="515" height="326" viewBox="0 0 515 326" xmlns="http://www.w3.org/2000/svg">
    <defs>
      <linearGradient id="panel" x1="0" y1="0" x2="0" y2="1">
        <stop offset="0" stop-color="#1b6aa6"/><stop offset="1" stop-color="#0a3c64"/>
      </linearGradient>
    </defs>
    <path d="M0 0 H510 L395 326 H0 Z" fill="#ffffff"/>
    <path d="M0 0 H500 L387 326 H0 Z" fill="url(#panel)"/>
  </svg>
  <h2 class="services-title">Our Services</h2>
  <div class="services-rule"></div>
  <ul class="services-list">
    <li class="current"><svg width="20" height="20" viewBox="0 0 20 20"><circle cx="10" cy="10" r="9" fill="#f08a24" stroke="#fff" stroke-width="1.5"/><path d="M6 10 H13 M10 7 L13 10 L10 13" stroke="#fff" stroke-width="2" fill="none"/></svg>Data mining and analysis</li>
    <li><svg width="20" height="20" viewBox="0 0 20 20"><circle cx="10" cy="10" r="9" fill="#f08a24" stroke="#fff" stroke-width="1.5"/><path d="M6 10 H13 M10 7 L13 10 L10 13" stroke="#fff" stroke-width="2" fill="none"/></svg>E-discovery and case management</li>
    <li><svg width="20" height="20" viewBox="0 0 20 20"><circle cx="10" cy="10" r="9" fill="#f08a24" stroke="#fff" stroke-width="1.5"/><path d="M6 10 H13 M10 7 L13 10 L10 13" stroke="#fff" stroke-width="2" fill="none"/></svg>E-discovery collection and analysis</li>
  </ul>

  <h2 class="feature-title">Data Mining and Analysis</h2>
  <div class="feature-rule"></div>
  <div class="feature-photo"><div role="img" aria-label="Photo: chalkboard with business intelligence keywords"></div></div>
  <p class="feature-text"><strong>Lorem ipsum dolor sit amet,</strong> consectetur adipiscing elit. Aliquam bibendum lacinia nisi, sit amet imperdiet odio. Class aptent taciti sociosqu ad litora torquent per conubia nostra, per inceptos himenaeos. Sed consectetur turpis ac facilisis cursus. Fusce ac dolor quam.</p>
  <a class="btn btn-more" href="#">More</a>

  <footer class="site-footer">
    <p class="copyright">© 2014 Veranth Systems. All rights reserved.</p>
    <div class="footer-brand"><span class="brand-dot"></span><span class="brand-name">VERANTH SYSTEMS</span></div>
  </footer>
</body>
</html>
```